Brochure Design Project

We are a payroll company. We offer a wide variety of products and services:
1. Payroll Processing
2. Employee Direct Deposit
3. Time and attendance
4. HR services
5. Employee Employee Benefits

I'd like to develop a one page template that uses a combination of our logo (attached), colors (attached) and possible a picture. The picture could be shown as an option as it may change based on the product or service.

Target Market(s)

Adults in the United States ages 22-50. Typically these people are accountants, human resource professionals or entrepreneurs. The payroll industry is dominated by 3 large payroll processors, QLM, Wendrafy and Tolvarex. These companies are very impersonal and make it difficult to resolve issues when they arise. We have grown to over 400 clients by being the opposite of the big guys,

Industry/Entity Type

It Company

Font styles to use
Sans Serif

Requirements
Must have
• The brochure can be one or two pages.
Nice to have
• I'll know it when I see it but I can't describe it. I have attached a few brochures that have caught my eye.
Should not have
• No cartoons. No money signs. Hip, new, fresh are words I'd use to describe the winning product. Of the three people I described in my target market, the entrepreneur is the market I'd most like to target.

```html
<!DOCTYPE html>
<html lang="en">
<head>
<meta charset="utf-8">
<title>Paystead Partners – Payroll Services</title>
<link rel="stylesheet" href="https://fonts.googleapis.com/css2?family=Arvo:wght@400;700&family=Open+Sans:wght@400;600;700&display=swap">
<style>
  :root {
    --grey-bg: #e1e1e1;
    --navy: #0b2d5f;
    --white: #ffffff;
    --headline: #555555;
    --ink: #222222;
    --frame: #9a9a9a;
    --photo-dark: #1c1c1e;
    --photo-light: #d9cfc4;
  }
  html, body { margin: 0; padding: 0; overflow: hidden; background: var(--white); }
  .brochure {
    position: relative;
    width: 849px;
    height: 1200px;
    overflow: hidden;
    background: var(--white);
    box-sizing: border-box;
    border: 1px solid var(--frame);
    font-family: "Open Sans", Arial, sans-serif;
    color: var(--ink);
  }
  .backdrop { position: absolute; inset: 0; }
  .portrait {
    position: absolute;
    left: 528px;
    top: 78px;
    width: 298px;
    height: 622px;
    border-radius: 150px 150px 0 0;
    background: linear-gradient(180deg, var(--photo-light) 0%, #b09a7a 22%, #6d625a 38%, var(--photo-dark) 55%, var(--photo-dark) 100%);
  }
  .tagline {
    position: absolute;
    left: 74px;
    top: 84px;
    margin: 0;
    font-family: "Arvo", Georgia, serif;
    font-weight: 400;
    font-size: 33px;
    line-height: 31px;
    letter-spacing: 0.2px;
    color: var(--headline);
  }
  .quote-mark {
    position: absolute;
    font-family: "Arvo", Georgia, serif;
    font-weight: 700;
    font-size: 110px;
    line-height: 1;
    color: var(--navy);
  }
  .quote-open { left: 26px; top: 34px; }
  .quote-close { left: 490px; top: 114px; }
  .brand-name {
    position: absolute;
    left: 78px;
    top: 204px;
    margin: 0;
    font-weight: 700;
    font-size: 46px;
    line-height: 52px;
    color: var(--navy);
  }
  .intro {
    position: absolute;
    left: 63px;
    top: 416px;
    width: 440px;
    color: var(--white);
    font-weight: 600;
    font-size: 18.5px;
    line-height: 24px;
  }
  .intro p { margin: 0 0 18px; }
  .intro ol { margin: 0; padding: 0; list-style: none; line-height: 22.5px; }
  .services {
    position: absolute;
    left: 69px;
    top: 756px;
    width: 715px;
    font-size: 14.3px;
    line-height: 19.5px;
  }
  .services h2 {
    margin: 0 0 9px;
    font-family: "Arvo", Georgia, serif;
    font-weight: 400;
    font-size: 30px;
    line-height: 36px;
    color: #333333;
  }
  .services p { margin: 0 0 19px; }
  .services ul { margin: 0 0 19px; padding: 0; list-style: none; font-weight: 700; }
</style>
</head>
<body>
  <main class="brochure">
    <svg class="backdrop" width="849" height="1200" viewBox="0 0 849 1200" aria-hidden="true">
      <rect x="0" y="0" width="849" height="760" fill="var(--grey-bg)"/>
      <path d="M0 402 Q456 280 849 402 L849 730 Q456 620 0 730 Z" fill="var(--navy)"/>
      <path d="M0 730 Q456 620 849 730 L849 1200 L0 1200 Z" fill="var(--white)"/>
    </svg>

    <div class="portrait" role="img" aria-label="Photo of a smiling businesswoman in a dark suit and glasses writing in a notebook"></div>

    <span class="quote-mark quote-open">&ldquo;</span>
    <h1 class="tagline">INNOVATIVE SOLUTIONS<br>THAT DELIEVER VALUE</h1>
    <span class="quote-mark quote-close">&rdquo;</span>

    <p class="brand-name">Paystead<br>Partners</p>

    <section class="intro">
      <p>We are a payroll company. We offer a wide<br>variety of products and services:</p>
      <ol>
        <li>1. Payroll Processing</li>
        <li>2. Employee Direct Deposit</li>
        <li>3. Time &amp; attendance</li>
        <li>4. HR services</li>
        <li>5. Employee Employee Benefits</li>
      </ol>
    </section>

    <section class="services">
      <h2>PAYROLL SERVICES</h2>
      <p>Paystead Partners offers exceptional payroll management services.&nbsp; Accurate and timely payroll managment is a basic requirement of every business.&nbsp; Utilize your resources better by partnering with Paystead Partners.</p>
      <p>Our comprehensive payroll management services and hands-on customer care allows you to implement payroll solutions that make sense for your business. Our services include:</p>
      <ul>
        <li>Payroll Processing</li>
        <li>Payroll Reporting</li>
        <li>Tax Administration</li>
        <li>Custom Payroll Solutions</li>
      </ul>
      <p>As your business evolves, we work along side you to reasses your options and make suggestions to improve your business efficacy. Allow us to handle your payroll management and give yourself more time to manage your business!</p>
    </section>
  </main>
</body>
</html>
```